Business card design to suit our website

Need a nice looking business card for our business based off images from our Website and provided images. The business card will require 2 different names (for the 2 owners). The business card should include images from our website, facebook (keel bracket works set) or the pictures provided. it should also contain all contact information.
Our website is www.keelbracketworks.com.au
Please dont use image from top bar of website. If images are used please use the ones of our product under the buy it now tab

Target Market(s)

Automotive

Industry/Entity Type

Automotive Part

Contact Information for Business Card

Business Name. contact details including names phone number email. logo
2 business cards needed with 2 different persons names and phone number.

Colors

Designer to choose colors to be used in the design.

Requirements
Must have
• whatever looks best

```html
<!DOCTYPE html>
<html lang="en">
<head>
<meta charset="utf-8">
<title>Steadfast – Business Card</title>
<link href="https://fonts.googleapis.com/css2?family=Exo+2:wght@500;700;800&family=Roboto:wght@400;500&display=swap" rel="stylesheet">
<style>
  :root {
    --page-bg: #ececec;
    --card-black: #141515;
    --card-black-mid: #2a2c2d;
    --card-white: #f7f7f7;
    --brand-red: #c0202c;
    --brand-red-deep: #8e1520;
    --text-white: #ffffff;
    --flag-grey: #cfcfcf;
    --car-grey: #bdbdbd;
  }
  * { margin: 0; padding: 0; box-sizing: border-box; }
  html, body {
    width: 1200px; height: 960px; overflow: hidden;
    background: var(--page-bg);
  }
  .canvas { position: relative; width: 1200px; height: 960px; }

  .card {
    position: absolute; width: 600px; height: 340px;
    border-radius: 18px; overflow: hidden;
  }

  /* Front */
  .card-front {
    left: 302px; top: 125px;
    background: radial-gradient(ellipse at 55% 30%, var(--card-black-mid) 0%, var(--card-black) 70%);
  }
  .brand-name {
    position: absolute; left: 40px; top: 70px;
    font-family: "Exo 2", sans-serif; font-weight: 800;
    font-size: 40px; line-height: 1; color: var(--brand-red);
    letter-spacing: 0.5px;
  }
  .brand-tagline {
    position: absolute; left: 66px; top: 126px;
    font-family: "Exo 2", sans-serif; font-weight: 500;
    font-size: 21px; color: var(--text-white);
  }
  .contact-list {
    position: absolute; left: 55px; top: 222px; list-style: none;
    font-family: "Roboto", sans-serif; font-size: 13.5px; color: var(--text-white);
  }
  .contact-list li { display: flex; align-items: center; height: 19.5px; }
  .contact-list li:first-child { font-size: 14.5px; font-weight: 500; }
  .contact-icon { width: 13px; height: 13px; margin-right: 8px; fill: var(--brand-red); }
  .person {
    position: absolute; right: 42px; top: 229px; text-align: right;
    font-family: "Roboto", sans-serif;
  }
  .person-name {
    font-family: "Exo 2", sans-serif; font-weight: 700;
    font-size: 22px; line-height: 1.05; color: var(--brand-red);
  }
  .person-title { font-size: 14px; font-weight: 500; color: var(--text-white); margin-top: 3px; }
  .accent-bar {
    position: absolute; right: 0; top: 228px; width: 11px; height: 42px;
    background: var(--brand-red);
  }

  /* Back */
  .card-back { left: 299px; top: 493px; background: var(--card-white); }
  .flag-area {
    position: absolute; left: 0; top: 0; width: 175px; height: 340px;
    background: linear-gradient(100deg, var(--flag-grey) 0%, #e6e6e6 55%, rgba(247,247,247,0) 100%);
  }
  .car-area {
    position: absolute; left: 130px; top: 28px; width: 330px; height: 196px;
    border-radius: 40% 45% 30% 30%;
    background: radial-gradient(ellipse at 50% 55%, var(--car-grey) 0%, #dcdcdc 60%, rgba(247,247,247,0) 100%);
  }
  .track-band {
    position: absolute; left: 0; width: 600px; background: var(--brand-red);
  }
  .track-band.upper { top: 257px; height: 32px; }
  .track-band.lower { top: 293px; height: 24px; }
  .back-brand-name {
    position: absolute; left: 0; width: 600px; top: 240px; text-align: center;
    font-family: "Exo 2", sans-serif; font-weight: 800;
    font-size: 38px; line-height: 1; color: var(--brand-red-deep);
  }
  .back-tagline {
    position: absolute; left: 0; width: 600px; top: 291px; text-align: center;
    font-family: "Exo 2", sans-serif; font-weight: 500;
    font-size: 20px; color: var(--text-white);
  }
</style>
</head>
<body>
<main class="canvas">

  <section class="card card-front" aria-label="Business card front">
    <div class="brand-name">Steadfast</div>
    <div class="brand-tagline">Keel Bracket Works Set</div>

    <ul class="contact-list">
      <li>
        <svg class="contact-icon" viewBox="0 0 16 16" aria-hidden="true"><path d="M3.6 1.2l2.3 2.6-1.4 2.1c.9 1.9 2.2 3.3 4.1 4.3l2.1-1.4 2.6 2.3-1.2 2.5C6.7 13.4 2.6 9.3 1.1 2.4z"/></svg>
        1300 555 184
      </li>
      <li>
        <svg class="contact-icon" viewBox="0 0 16 16" aria-hidden="true"><path d="M1 3h14v10H1zM2.5 4.5L8 9l5.5-4.5v-.3h-11z" fill-rule="evenodd"/></svg>
        dana@keelbracketworks.com.au
      </li>
      <li>
        <svg class="contact-icon" viewBox="0 0 16 16" aria-hidden="true"><circle cx="8" cy="8" r="7"/><path d="M5 4c2 1 1 3 3 3s1 3 3 4" stroke="#141515" stroke-width="1.4" fill="none"/></svg>
        www.keelbracketworks.com.au
      </li>
    </ul>

    <div class="person">
      <div class="person-name">DANA HOLLIS</div>
      <div class="person-title">CEO/FOUNDER</div>
    </div>
    <div class="accent-bar"></div>
  </section>

  <section class="card card-back" aria-label="Business card back">
    <div class="flag-area" role="img" aria-label="Waving chequered racing flag"></div>
    <div class="car-area" role="img" aria-label="Pencil drawing of a silver performance sedan"></div>
    <div class="track-band upper" role="img" aria-label="Red band with tyre tread marks"></div>
    <div class="track-band lower"></div>
    <div class="back-brand-name">Steadfast</div>
    <div class="back-tagline">Keel Bracket Works Set</div>
  </section>

</main>
</body>
</html>
```